Design of a Web Development Agency

We're a web development agency (we do not offer design services). We'd like to get a new website up and running. We do custom web application development - large scale applications in the financial, healthcare, automotive, and other industries.

We need the following types of pages designed:
1) Homepage
2) Blog
3) Services page
4) Packages page
4) Generic content
5) Contact Us form.

The design should be consistent with our current icon. We're looking for a clean, corporate, brand. We'd like the design to expand on the concepts in the logo - the use of the electrical wiring motif / the colors / etc.

We offer the following services: 1) Cobalto web hosting consulting, 2) custom application development, 3) Qel development, 4) Veltrix development.

We offer packages in numbers of hours. We have about 3-4 tiers of services - the number of hours versus the monthly invoice total. For example, 5 hours per month of $500.00, for example.

Target Market(s)

Corporate clients

Industry/Entity Type

Electrical

Colors
acd036
33b7a4
33a6d7
3176b5
876aae
b768aa
fbee3e

Requirements
Must have
• Responsive / mobile friendly design.
• An email submitting form on the contact us page
Nice to have
• We'd like a bit of San Francisco to come through (where we're located)
• A plorvo map of our address on the contact us page
Should not have
• Excessive imagery. We don't have a lot of imagery, so we'd basically have to go out and find stock photography to put in it's place, which we just don't really want to do. All imagery should be supplied by the designer (we'll pay any copyright fees, if applicable, you just have to send us a list of the links to the imagery. Max budget would be $100-$200 on imagery, but preferably as little as possible).

```html
<!DOCTYPE html>
<html lang="en">
<head>
<meta charset="utf-8">
<title>Norvane Web Works — Web Application Development Agency</title>
<link rel="stylesheet" href="https://fonts.googleapis.com/css2?family=Open+Sans:wght@400;600;700&family=Roboto:wght@300;400;500;700&display=swap">
<style>
:root{
  --green:#8dc63f;
  --green-dark:#7ab32e;
  --blue:#2f95d6;
  --blue-deep:#2478bd;
  --text:#555;
  --muted:#8a8a8a;
  --line:#dcdcdc;
  --grey-band:#f0f0f0;
  --footer:#3a3a3a;
  --footer-bottom:#2b2b2b;
  --white:#fff;
}
*{box-sizing:border-box;margin:0;padding:0}
html,body{width:1200px;height:3130px;overflow:hidden}
body{font-family:"Open Sans",Arial,sans-serif;color:var(--text);background:var(--white);font-size:13px;line-height:1.55}
section,header,footer{position:relative;width:1200px}

/* header */
.site-header{height:105px;border-bottom:1px solid var(--line)}
.brand{position:absolute;left:128px;top:18px;display:flex;align-items:center;gap:12px}
.brand-square{width:66px;height:66px;background:#3a3a3a;border:3px solid var(--green)}
.brand-name{font-family:"Roboto",sans-serif;font-weight:700;font-size:18px;color:#333;letter-spacing:.5px}
.top-contacts{position:absolute;right:128px;top:16px;display:flex;gap:26px;font-size:12px;color:#666}
.top-contacts span{display:flex;align-items:center;gap:7px}
.nav{position:absolute;right:128px;top:58px;display:flex;gap:36px;font-family:"Roboto",sans-serif;font-size:12px;font-weight:500;color:#777;letter-spacing:.5px}
.nav a{color:inherit;text-decoration:none;padding-bottom:8px}
.nav a.active{color:var(--green);border-bottom:2px solid var(--green)}

/* hero */
.hero{height:455px;background:linear-gradient(180deg,#3aa3e0 0%,#2a86cc 100%);overflow:hidden;color:var(--white)}
.hero-art{position:absolute;left:240px;top:20px;width:720px;height:220px;background:radial-gradient(ellipse at center,rgba(255,255,255,.12) 0%,rgba(255,255,255,0) 70%)}
.device{position:absolute;border-radius:10px}
.device-phones{left:100px;top:70px;width:230px;height:270px;background:linear-gradient(160deg,#e9eef2,#9fb0bf)}
.device-tablet{left:860px;top:180px;width:250px;height:230px;background:linear-gradient(160deg,#f4f6f8,#aab7c4)}
.hero-icon{position:absolute;left:550px;top:150px;width:100px;height:100px;border-radius:50%;background:var(--green);border:4px solid var(--white);display:flex;align-items:center;justify-content:center}
.hero-title{position:absolute;left:0;right:0;top:272px;text-align:center;font-family:"Roboto",sans-serif}
.hero-title small{display:block;font-size:30px;font-weight:300}
.hero-title strong{display:block;font-size:38px;font-weight:400;line-height:1.2}

/* section titles */
.title-box{position:absolute;left:220px;width:760px;background:var(--white);border:1px solid var(--line);text-align:center;padding:22px 60px 24px}
.title-box h2{font-family:"Roboto",sans-serif;font-weight:400;font-size:30px;color:#444;letter-spacing:.5px;margin-bottom:12px;white-space:nowrap}
.title-box h2 em{font-style:normal;color:var(--green)}
.title-box p{font-size:12px;color:var(--muted);line-height:1.6}
.title-box p b{color:var(--blue);font-weight:400}
.spine{position:absolute;left:599px;width:2px;background:#e6e6e6}

/* solutions */
.solutions{height:620px}
.service{position:absolute;width:330px;display:flex;gap:16px}
.service .ico{flex:0 0 58px;height:58px;border-radius:50%;background:var(--green);display:flex;align-items:center;justify-content:center}
.service h3{font-family:"Roboto",sans-serif;font-size:15px;font-weight:500;color:#444;margin-bottom:6px}
.service p{font-size:12px;color:var(--muted)}
.service.right{flex-direction:row-reverse;text-align:left}
.btn-ghost{position:absolute;left:530px;top:397px;width:140px;height:34px;border:1px solid #bbb;background:var(--white);font-family:"Roboto",sans-serif;font-size:12px;color:#666;display:flex;align-items:center;justify-content:center;letter-spacing:.5px}

/* packages */
.packages{height:590px;background:var(--grey-band)}
.plans{position:absolute;left:150px;top:250px;width:900px;display:flex}
.plan{width:180px;height:280px;background:var(--white);border:1px solid var(--line);text-align:center;padding-top:26px}
.plan .price{font-family:"Roboto",sans-serif;font-size:30px;color:var(--blue);font-weight:300}
.plan .hours{font-size:11px;color:var(--blue);margin-bottom:22px}
.plan h4{font-family:"Roboto",sans-serif;font-size:18px;color:var(--blue);font-weight:400;letter-spacing:1px;margin-bottom:10px}
.plan p{font-size:11px;color:var(--muted);padding:0 18px;margin-bottom:20px}
.plan .sign{display:inline-block;border:1px solid var(--blue);color:var(--blue);font-size:11px;font-weight:600;padding:6px 14px}
.plan.featured{background:var(--green);border-color:var(--green);margin-top:-40px;height:360px;color:var(--white);padding-top:34px}
.plan.featured .price,.plan.featured .hours,.plan.featured h4,.plan.featured p{color:var(--white)}
.plan.featured .sign{background:var(--white);color:var(--green);border-color:var(--white)}
.plan.featured .off{font-size:11px;margin-top:-18px;margin-bottom:22px}

/* portfolio */
.portfolio{height:490px}
.works{position:absolute;left:150px;top:210px;width:900px;display:flex;gap:45px}
.work{width:270px}
.work .shot{height:190px;border:1px solid var(--line);margin-bottom:12px}
.work h5{font-size:14px;font-weight:600;color:#444}
.work span{font-size:12px;color:var(--green)}

/* testimonials */
.testimonials{height:490px}
.quotes{position:absolute;left:150px;top:260px;width:900px;display:flex;gap:60px}
.quote{width:260px;font-size:12px;color:var(--muted)}
.quote a{display:block;margin-top:14px;color:var(--blue);text-decoration:none}
.dots{position:absolute;left:0;right:0;top:450px;display:flex;justify-content:center;gap:8px}
.dots i{width:9px;height:9px;border-radius:50%;background:#ccc}
.dots i.on{background:var(--blue)}

/* footer */
.site-footer{height:340px;background:var(--footer);color:#ccc}
.footer-col{position:absolute;top:40px}
.footer-col h6{font-family:"Roboto",sans-serif;font-size:15px;font-weight:500;color:var(--white);margin-bottom:30px;letter-spacing:.5px}
.form-lead{font-size:13px;font-weight:600;color:var(--white);margin-bottom:18px}
.fields{display:grid;grid-template-columns:200px 200px;gap:12px 20px}
.field{height:28px;border-bottom:1px solid #555;font-size:11px;color:#999;padding-top:6px}
.btn-blue{display:inline-flex;align-items:center;justify-content:center;background:var(--blue);color:var(--white);font-size:11px;font-weight:600;height:28px;padding:0 16px}
.info-grid{display:grid;grid-template-columns:220px 200px;gap:20px 20px}
.info{display:flex;gap:10px;font-size:11px;color:#aaa}
.info b{display:block;color:var(--white);font-weight:600;font-size:11px}
.info .dot{flex:0 0 30px;height:30px;border-radius:50%;background:#555;display:flex;align-items:center;justify-content:center}
.socials{display:flex;gap:6px;margin-top:6px}
.socials i{width:22px;height:22px;border-radius:50%;background:#5c5c5c}
.newsletter{display:flex;gap:6px;margin-top:14px}
.newsletter .input{width:170px;height:28px;background:#4a4a4a;font-size:11px;color:#999;padding:6px 10px}
.footer-bottom{height:40px;background:var(--footer-bottom);color:#888;font-size:11px;text-align:center;padding-top:12px;position:relative}
.to-top{position:absolute;left:586px;top:-14px;width:28px;height:28px;border-radius:50%;background:var(--blue);display:flex;align-items:center;justify-content:center}
</style>
</head>
<body>

<header class="site-header">
  <div class="brand"><div class="brand-square"></div><div class="brand-name">NORVANE WEB WORKS</div></div>
  <div class="top-contacts">
    <span><svg width="14" height="14" viewBox="0 0 24 24"><path d="M6.6 10.8a15 15 0 0 0 6.6 6.6l2.2-2.2c.3-.3.7-.4 1-.2 1.1.4 2.3.6 3.6.6.6 0 1 .4 1 1V20c0 .6-.4 1-1 1A17 17 0 0 1 3 4c0-.6.4-1 1-1h3.5c.6 0 1 .4 1 1 0 1.3.2 2.5.6 3.6.1.3 0 .7-.2 1z" fill="#2f95d6"/></svg>(415) 555-0142</span>
    <span><svg width="14" height="14" viewBox="0 0 24 24"><rect x="2" y="5" width="20" height="14" rx="2" fill="#2f95d6"/><path d="M2 6l10 7 10-7" stroke="#fff" stroke-width="1.6" fill="none"/></svg>hello@norvane.co</span>
  </div>
  <nav class="nav">
    <a class="active" href="#">HOME</a><a href="#">BLOG</a><a href="#">SERVICES</a><a href="#">PACKAGES</a><a href="#">GENERAL</a><a href="#">CONTACT US</a>
  </nav>
</header>

<section class="hero">
  <div class="hero-art" role="img" aria-label="Circuit wiring illustration linking the industries served"></div>
  <div class="device device-phones" role="img" aria-label="Phones showing responsive agency websites"></div>
  <div class="device device-tablet" role="img" aria-label="Tablet showing an agency web application"></div>
  <div class="hero-icon">
    <svg width="50" height="44" viewBox="0 0 50 44" fill="#fff"><rect x="17" y="0" width="16" height="12"/><rect x="0" y="30" width="14" height="12"/><rect x="18" y="30" width="14" height="12"/><rect x="36" y="30" width="14" height="12"/><path d="M24 12h2v8h-2zM6 20h38v2H6zM6 20h2v10H6zM24 20h2v10h-2zM42 20h2v10h-2z"/></svg>
  </div>
  <div class="hero-title"><small>We're a</small><strong>Web Application<br>Development Agency</strong></div>
</section>

<section class="solutions">
  <div class="spine" style="top:0;height:40px"></div>
  <div class="title-box" style="top:40px">
    <h2>WE OFFERING <em>BEST SOLUTION</em></h2>
    <p>Clear, reliable software for teams that run on data, built with care in the <b>city by the bay</b> for clients in finance, healthcare, automotive and other industries.</p>
  </div>
  <div class="service" style="left:220px;top:250px">
    <div class="ico"><svg width="26" height="26" viewBox="0 0 24 24" fill="#fff"><path d="M6 18a4 4 0 0 1 0-8 6 6 0 0 1 11.6-1.6A4.8 4.8 0 0 1 18 18z"/></svg></div>
    <div><h3>Cobalto Web Hosting Consulting</h3><p>We help teams plan, migrate and tune their hosting so apps stay fast, secure and ready to scale.</p></div>
  </div>
  <div class="service right" style="left:650px;top:250px">
    <div class="ico"><svg width="26" height="26" viewBox="0 0 24 24" fill="none" stroke="#fff" stroke-width="2"><rect x="3" y="4" width="18" height="13" rx="1"/><path d="M8 21h8M12 17v4"/></svg></div>
    <div><h3>Web Application Development</h3><p>With over ten years of experience we build large custom web applications for finance, healthcare and more.</p></div>
  </div>
  <div class="btn-ghost">FIND OUT MORE</div>
  <div class="service" style="left:220px;top:470px">
    <div class="ico"><svg width="22" height="28" viewBox="0 0 16 24" fill="none" stroke="#fff" stroke-width="2"><rect x="2" y="1" width="12" height="22" rx="2"/><path d="M6 19h4"/></svg></div>
    <div><h3>Mobile Application Development</h3><p>We ship native Qel and Veltrix apps that share one solid back end with your web platform.</p></div>
  </div>
  <div class="service right" style="left:650px;top:470px">
    <div class="ico"><svg width="22" height="28" viewBox="0 0 16 24" fill="none" stroke="#fff" stroke-width="2"><rect x="2" y="1" width="12" height="22" rx="2"/><path d="M2 5h12M2 18h12"/></svg></div>
    <div><h3>Veltrix Development</h3><p>Our team builds and maintains Veltrix apps for phones and tablets with a focus on clean, stable code.</p></div>
  </div>
</section>

<section class="packages">
  <div class="title-box" style="top:30px">
    <h2>WE OFFER THE PACKAGES <em>BETTER THAN OTHER</em></h2>
    <p>Buy a block of hours each month and use them as you need, from small fixes to <b>full feature builds</b>, with one simple invoice and no surprise costs.</p>
  </div>
  <div class="plans">
    <div class="plan"><div class="price">$1,500</div><div class="hours">50 hours per month</div><h4>STARTER</h4><p>A steady block of hours for small teams and ongoing upkeep.</p><span class="sign">SIGN UP NOW!</span></div>
    <div class="plan"><div class="price">$3,000</div><div class="hours">100 hours per month</div><h4>INTERMEDIATE</h4><p>Room for new features plus regular support every month.</p><span class="sign">SIGN UP NOW!</span></div>
    <div class="plan featured"><div class="price">$6,500</div><div class="hours">200 hours per month</div><div class="off">( 15% OFF )</div><h4>ADVANCED</h4><p>A dedicated team for growing products with large roadmaps.</p><span class="sign">SIGN UP NOW!</span></div>
    <div class="plan"><div class="price">$11,250</div><div class="hours">350 hours per month</div><h4>ULTIMATE</h4><p>Full scale delivery for complex apps across many platforms.</p><span class="sign">SIGN UP NOW!</span></div>
    <div class="plan"><div class="price">$625*</div><div class="hours">6 hours per month</div><h4>HOSTING</h4><p>Managed hosting, monitoring and updates for one application.</p><span class="sign">SIGN UP NOW!</span></div>
  </div>
</section>

<section class="portfolio">
  <div class="spine" style="top:0;height:40px"></div>
  <div class="title-box" style="top:40px;padding-bottom:28px">
    <h2>OUR LATEST <em>PORTFOLIO</em></h2>
  </div>
  <div class="works">
    <div class="work"><div class="shot" role="img" aria-label="Halden Funds website shown on desktop and phone" style="background:linear-gradient(160deg,#eef3f7,#9ab6cf)"></div><h5>Halden Funds</h5><span>haldenfunds.com</span></div>
    <div class="work"><div class="shot" role="img" aria-label="Brightwave website shown on desktop and phone" style="background:linear-gradient(160deg,#f3f3f3,#b4b9bf)"></div><h5>Brightwave</h5><span>brightwave.co</span></div>
    <div class="work"><div class="shot" role="img" aria-label="Novira website shown on desktop and phone" style="background:linear-gradient(160deg,#e8f0f8,#4d7fb8)"></div><h5>Novira</h5><span>novira.io</span></div>
  </div>
</section>

<section class="testimonials">
  <div class="spine" style="top:0;height:40px"></div>
  <div class="title-box" style="top:40px">
    <h2>WHAT OUR <em>HAPPY CLIENT SAY</em></h2>
    <p>Long term partners share how working with our team helped them <b>launch faster</b> and keep their platforms running smoothly every day.</p>
  </div>
  <div class="quotes">
    <div class="quote">The team rebuilt our client portal on time and on budget. Support has been quick and friendly, and the new app handles three times the traffic we had before without any trouble.<a href="#">— Client Name</a></div>
    <div class="quote">Clear plans, honest estimates and clean code. Our patient records system is faster and easier to use, and our staff picked it up in days rather than weeks after launch.<a href="#">— Client Name</a></div>
    <div class="quote">Monthly hours work well for us. We add features as we need them and always know the cost up front. It feels like having our own engineering team in house.<a href="#">— Client Name</a></div>
  </div>
  <div class="dots"><i class="on"></i><i></i><i></i></div>
</section>

<footer>
  <div class="site-footer">
    <div class="footer-col" style="left:150px">
      <h6>CONTACT FORM</h6>
      <div class="form-lead">SAY HELLO TO US, WE WILL ANSWER AS SOON AS POSSIBLE.</div>
      <div class="fields">
        <div class="field">Enter Your Name</div><div class="field">Enter Your Email</div>
        <div class="field">Enter Your Phone Number</div><div class="field">Enter Your Subject</div>
        <div class="field">Enter Your Message</div><div></div>
      </div>
      <div style="margin-top:34px"><span class="btn-blue">SEND MESSAGE</span></div>
    </div>
    <div class="footer-col" style="left:620px">
      <h6>CONTACT INFORMATION</h6>
      <div class="info-grid">
        <div class="info"><div class="dot"><svg width="12" height="14" viewBox="0 0 24 28" fill="#fff"><path d="M12 0a10 10 0 0 0-10 10c0 8 10 18 10 18s10-10 10-18A10 10 0 0 0 12 0zm0 14a4 4 0 1 1 0-8 4 4 0 0 1 0 8z"/></svg></div><div><b>WORKING LOCATION</b>240 Harbor Lane, Suite 5<br>San Francisco, CA 94100</div></div>
        <div class="info"><div class="dot"><svg width="13" height="13" viewBox="0 0 24 24"><path d="M6.6 10.8a15 15 0 0 0 6.6 6.6l2.2-2.2c.3-.3.7-.4 1-.2 1.1.4 2.3.6 3.6.6.6 0 1 .4 1 1V20c0 .6-.4 1-1 1A17 17 0 0 1 3 4c0-.6.4-1 1-1h3.5c.6 0 1 .4 1 1 0 1.3.2 2.5.6 3.6.1.3 0 .7-.2 1z" fill="#fff"/></svg></div><div><b>ONLINE NUMBER</b>Pick up and call us now<br>(415) 555-0142</div></div>
        <div class="info"><div class="dot"><svg width="13" height="11" viewBox="0 0 24 18"><rect x="1" y="1" width="22" height="16" rx="2" fill="#fff"/><path d="M1 2l11 8 11-8" stroke="#555" stroke-width="1.6" fill="none"/></svg></div><div><b>EMAIL</b>Email us for a quote<br>hello@norvane.co</div></div>
        <div class="info"><div class="dot"></div><div><b>STAY CONNECTED</b><div class="socials"><i></i><i></i><i></i><i></i></div></div></div>
      </div>
      <h6 style="margin-top:30px;margin-bottom:0">SUBSCRIBE OUR NEWSLETTER</h6>
      <div class="newsletter"><div class="input">Enter Your Email Address</div><span class="btn-blue">SUBSCRIBE</span></div>
    </div>
  </div>
  <div class="footer-bottom">
    <div class="to-top"><svg width="12" height="8" viewBox="0 0 12 8"><path d="M1 7l5-5 5 5" stroke="#fff" stroke-width="2" fill="none"/></svg></div>
    © 2015 Norvane Web Works. All Rights Reserved
  </div>
</footer>

</body>
</html>
```